Newspaper Ad

Please create an ad for a newspaper that is 10.5 wide and 13 inches long. Please highlight the features of the property and ensure that the name of our firm (Birchwood Hollow Estates) is the same size as our phone number which is 717-390-5168.

Pembrook's Landing and The residences at 9 N. Fern
9 N. Fern Street, Quarryville PA

Now leasing 1, 2 & 3 bedroom units available this spring. Newley renovated apartments with stainless appliances, hardwood floors, granite countertops, in unit laundry. Includes water, sewer trash and off street parking. 1200sq first floor retail available.

717.390.5168 or www.BirchwoodHollowEstates.example for details.

```html
<!DOCTYPE html>
<html lang="en">
<head>
<meta charset="utf-8">
<title>Now Leasing – Pembrook's Landing</title>
<link href="https://fonts.googleapis.com/css2?family=Poppins:wght@400;500;600;700&display=swap" rel="stylesheet">
<style>
  :root {
    --stage: #dcdcda;
    --ink-dark: #292526;
    --teal: #00a9bd;
    --teal-band: #00aabf;
    --white: #ffffff;
    --rule: #8d8a8b;
    --text-dark: #231f20;
    --brand-size: 40px;
  }
  * { margin: 0; padding: 0; box-sizing: border-box; }
  html, body {
    width: 1200px; height: 1200px; overflow: hidden;
    background: var(--stage);
    font-family: "Poppins", sans-serif;
  }
  .ad {
    position: absolute; left: 114px; top: 0;
    width: 971px; height: 1200px;
    background: var(--ink-dark);
    overflow: hidden;
  }
  .ad__rendering {
    position: absolute; left: 0; top: 0; width: 971px; height: 560px;
    background: linear-gradient(180deg,
      #7f97c4 0%, #c9d3e2 18%, #e9ecef 30%, #8f948d 48%,
      #7c817b 62%, #bfc0c2 70%, #3a3536 80%, var(--ink-dark) 100%);
  }
  .ad__headline { position: absolute; left: 0; width: 100%; text-align: center; }
  .ad__kicker { top: 574px; font-size: 33px; font-weight: 600; color: var(--teal); }
  .ad__kicker .ad__kicker-units { color: var(--white); }
  .ad__title {
    top: 622px; font-size: 63px; font-weight: 700; color: var(--teal);
    letter-spacing: 2px; line-height: 1.2;
  }
  .ad__rule {
    position: absolute; left: 88px; width: 808px; height: 2px;
    background: linear-gradient(90deg, transparent, #d9d9d9 50%, transparent);
  }
  .ad__rule--top { top: 720px; }
  .ad__rule--bottom { top: 771px; }
  .ad__address {
    position: absolute; top: 733px; left: 0; width: 100%; text-align: center;
    font-size: 18px; font-weight: 600; color: var(--white);
  }
  .features {
    position: absolute; left: 52px; top: 828px; width: 868px; height: 150px;
    border: 1.5px solid var(--rule); border-top: none;
  }
  .features__frame-top { position: absolute; top: 0; height: 1.5px; background: var(--rule); }
  .features__frame-top--left { left: 0; width: 86px; }
  .features__frame-top--right { right: 0; width: 105px; }
  .features__intro {
    position: absolute; top: -20px; left: 0; width: 100%; text-align: center;
    font-size: 28px; font-weight: 400; color: var(--white);
  }
  .features__row {
    position: absolute; left: 0; width: 100%;
    display: flex; justify-content: center; align-items: center;
    font-size: 18.5px; color: var(--white);
  }
  .features__row--one { top: 38px; }
  .features__row--two { top: 84px; }
  .features__sep {
    display: inline-block; width: 2px; height: 24px; background: var(--white);
    margin: 0 28px;
  }
  .retail-note {
    position: absolute; top: 996px; left: 0; width: 100%; text-align: center;
    font-size: 20px; font-weight: 600; color: var(--teal);
  }
  .contact-band {
    position: absolute; left: 0; top: 1054px; width: 971px; height: 146px;
    background: var(--teal-band);
  }
  .brand {
    position: absolute; left: 40px; top: 23px; width: 390px; height: 100px;
    background: #f2f2f2; border: 1.5px solid var(--text-dark);
    display: flex; align-items: center; justify-content: center; text-align: center;
    font-size: var(--brand-size); font-weight: 600; line-height: 1.08; color: var(--text-dark);
  }
  .contact__phone {
    position: absolute; left: 462px; top: 28px; height: 56px;
    display: flex; align-items: center; gap: 20px;
    font-size: var(--brand-size); font-weight: 600; color: var(--text-dark);
  }
  .contact__web {
    position: absolute; left: 468px; top: 94px; height: 36px;
    display: flex; align-items: center; gap: 20px;
    font-size: 19px; font-weight: 500; color: var(--text-dark);
  }
</style>
</head>
<body>
  <main class="ad">
    <div class="ad__rendering" role="img" aria-label="Architectural rendering of the renovated two-storey corner building with porches, under a blue cloudy sky"></div>

    <p class="ad__headline ad__kicker">NOW LEASING <span class="ad__kicker-units">1, 2 &amp; 3 BEDROOM</span> UNITS</p>
    <h1 class="ad__headline ad__title">AVAILABLE THIS SPRING</h1>

    <div class="ad__rule ad__rule--top"></div>
    <p class="ad__address">Pembrook's Landing and The Residences at 9 N. Fern Street, Quarryville PA</p>
    <div class="ad__rule ad__rule--bottom"></div>

    <section class="features">
      <span class="features__frame-top features__frame-top--left"></span>
      <span class="features__frame-top features__frame-top--right"></span>
      <h2 class="features__intro">Newly renovated apartments with</h2>
      <div class="features__row features__row--one">
        <span>off street parking</span><span class="features__sep"></span>
        <span>granite countertops</span><span class="features__sep"></span>
        <span>includes water, sewer, trash</span>
      </div>
      <div class="features__row features__row--two">
        <span>stainless appliances</span><span class="features__sep"></span>
        <span>hardwood floors</span><span class="features__sep"></span>
        <span>in unit laundry</span>
      </div>
    </section>

    <p class="retail-note">1,200 sq ft first floor retail space also available</p>

    <footer class="contact-band">
      <div class="brand">Birchwood<br>Hollow Estates</div>
      <div class="contact__phone">
        <svg width="34" height="34" viewBox="0 0 24 24" aria-hidden="true">
          <path fill="#231f20" d="M6.6 10.8a15.1 15.1 0 0 0 6.6 6.6l2.2-2.2a1 1 0 0 1 1-.25 11.4 11.4 0 0 0 3.6.57 1 1 0 0 1 1 1V20a1 1 0 0 1-1 1A17 17 0 0 1 3 4a1 1 0 0 1 1-1h3.5a1 1 0 0 1 1 1c0 1.25.2 2.45.57 3.57a1 1 0 0 1-.25 1z"/>
          <path fill="none" stroke="#231f20" stroke-width="1.6" stroke-linecap="round" d="M14 3.5a7 7 0 0 1 6.5 6.5M14 7a3.5 3.5 0 0 1 3 3"/>
        </svg>
        <span>717.390.5168</span>
      </div>
      <div class="contact__web">
        <svg width="22" height="22" viewBox="0 0 24 24" aria-hidden="true">
          <g fill="none" stroke="#231f20" stroke-width="1.6">
            <circle cx="12" cy="12" r="10"/>
            <ellipse cx="12" cy="12" rx="4.5" ry="10"/>
            <path d="M2 12h20M4 6.5h16M4 17.5h16"/>
          </g>
        </svg>
        <span>www.BirchwoodHollowEstates.example</span>
      </div>
    </footer>
  </main>
</body>
</html>
```